Internationales Familienunternehmen sucht Designvorschläge für Broschüre/Folder
Zielgruppe
Unser Unternehmen besteht aus 4 aktiven Sparten:
gastrosystems | elektrosystems | servicepartner | miratone wobak ideas
Alle Sparten sollen mit einem Layout bedient werden. Ziel wäre es aber z.B. auf der Titelseite im oberen Bereich die jeweiligen Sparten erkennen zu können und das jeweilige Prospektthema klein. Sodass man z.B. in einem Prospektständer die verschiedenen Prospekte auf einen Griff unterscheiden udn entnehmen kann.
Das Design muss verschiedenen Zielgruppen gefallen, daher muss das Layout modern, jung und dem neuen Logo entsprechend sein.
Aufgabenstellung
Wir haben unser Logo mit Anfang 2014 einem kompletten Redesign unterzogen und benötigen jetzt ein modernes und ansprechendes "passendes" Layout für unsere Produktbroschüren und -folder. Gesucht ist also Layoutvorschlag für Umschlag und Innenteil zur Präsentation von Produkten, Referenzen und natürlich entsprechenden Textflächen.
Als Ideenvolage kann unsere derzeit entstehende Website dienen: http://new.wobak-beispiel.net/
Bitte NICHT (!!!) an unserer bestehenden Website orientieren. www.wobak-beispiel.net ist nur noch kurze Zeit online!!! ACHTUNG!!!

```html
<!DOCTYPE html>
<html lang="de">
<head>
<meta charset="utf-8">
<title>Gastroschankanlagen – Broschüre Innenteil</title>
<link rel="stylesheet" href="https://fonts.googleapis.com/css2?family=Open+Sans:wght@300;400;600;700;800&display=swap">
<style>
:root{
  --stage:#d6d6d6;
  --paper:#ffffff;
  --ink:#3a3a3a;
  --ink-soft:#6b6b6b;
  --accent:#e8501c;
  --accent-soft:#f08a3c;
  --fold:#e6e6e6;
  --photo-dark:#2a1d17;
  --photo-copper:#b2643a;
}
*{box-sizing:border-box;margin:0;padding:0}
html,body{width:1200px;height:848px;overflow:hidden}
body{background:var(--stage);font-family:"Open Sans",Arial,sans-serif;color:var(--ink);position:relative}
.spread{position:absolute;left:60px;top:70px;width:1080px;height:708px;display:flex;box-shadow:0 12px 30px rgba(0,0,0,.25)}
.page{position:relative;width:540px;height:708px;background:var(--paper)}
.page--left{background:linear-gradient(90deg,var(--paper) 92%,var(--fold))}
.page--right{background:linear-gradient(90deg,var(--fold),var(--paper) 8%)}

/* left page */
.intro-title{position:absolute;left:40px;top:46px;font-weight:400;font-size:40px;line-height:1.08;letter-spacing:-.5px}
.intro-title .brand{color:var(--accent);font-weight:600}
.intro-sub{position:absolute;left:40px;top:142px;width:400px;font-size:17px;line-height:1.25;font-weight:300}
.cols{position:absolute;left:40px;top:222px;width:460px;display:flex;gap:26px}
.col{width:217px;font-size:10.5px;line-height:1.55;color:var(--ink-soft)}
.col p{margin-bottom:12px;text-align:justify}
.benefits{list-style:none;margin:4px 0 14px}
.benefits li{position:relative;padding-left:14px;font-size:10.5px;line-height:1.6;color:var(--ink)}
.benefits li::before{content:"";position:absolute;left:0;top:6px;width:6px;height:6px;background:var(--accent)}
.tablet{position:absolute;left:40px;top:530px;width:190px;height:130px;border-radius:10px;background:linear-gradient(135deg,#1e1e1e,#4a4a4a 60%,#2b2b2b)}

/* right page */
.range-intro{position:absolute;left:250px;top:30px;width:250px;font-size:10px;line-height:1.5;color:var(--ink-soft);text-align:right}
.range-title{position:absolute;left:50px;top:78px;font-weight:800;font-size:34px;line-height:1.2;color:var(--accent);letter-spacing:-.3px}
.range-sub{position:absolute;left:50px;top:124px;font-size:16px;font-weight:600;color:var(--accent-soft);letter-spacing:1px}
.products{position:absolute;left:50px;top:166px;width:450px;display:flex;justify-content:space-between}
.product{width:130px;height:62px;border-radius:4px;background:linear-gradient(180deg,#f2f2f2,#cfd3d6)}
.tap-photo{position:absolute;left:30px;top:250px;width:490px;height:270px;background:linear-gradient(120deg,var(--photo-dark) 10%,var(--photo-copper) 45%,#e3b48a 60%,var(--photo-dark) 95%)}
.references{position:absolute;left:30px;top:545px;width:490px;display:flex;justify-content:space-around;align-items:center;height:90px}
.reference{display:flex;align-items:center;gap:8px;font-size:13px;font-weight:600;color:var(--ink)}
.reference .dot{width:10px;height:10px;border-radius:50%;background:var(--ink)}
</style>
</head>
<body>
<div class="spread">
  <section class="page page--left">
    <h1 class="intro-title">Wie <span class="brand">wobak</span> ist<br>Ihre Schankanlage?</h1>
    <p class="intro-sub">WOBAK Gastrosystems setzt Maßstäbe für moderne Schank- und Abrechnungssysteme.</p>
    <div class="cols">
      <div class="col">
        <p>Alle Einnahmen werden registriert, egal ob durch Getränkeverkauf oder durch Speisen im Restaurant. Unsere Systeme sorgen für sauberen Ausschank und schnelle Abrechnung. Mit der richtigen Schankanlage behalten Sie jederzeit den Überblick über Bestand, Umsatz und Qualität. So lassen sich alle Abläufe im Betrieb einfach steuern und auswerten.</p>
      </div>
      <div class="col">
        <p>Alle Geräte der MIRATONE Serie können einzeln oder im Verbund betrieben werden. Die Bedienung erfolgt direkt am Zapfhahn.</p>
        <p>Und das Beste: die innovativen Komponenten werden seit Jahren in unserem Haus entwickelt und gefertigt. Der modulare Aufbau erlaubt eine einfache Erweiterung Ihrer Anlage.</p>
        <ul class="benefits">
          <li>Gewinnoptimierung</li>
          <li>Optimaler und schneller Arbeitsablauf</li>
          <li>Höchste Getränkequalität</li>
          <li>Effizientes Controlling</li>
        </ul>
        <p>Mit der MIRATONE Serie wurde der Schankbereich revolutioniert: moderne Technik, klares Design und robuste Verarbeitung für jeden Betrieb.</p>
      </div>
    </div>
    <div class="tablet" role="img" aria-label="Tablet mit Abrechnungssoftware"></div>
  </section>

  <section class="page page--right">
    <p class="range-intro">Mengenerfassung und Abrechnung für Schankanlagen mit bis zu zwölf Leitungen, flexibel konfigurierbar für Bar, Restaurant und Hotel.</p>
    <h2 class="range-title">Gastroschankanlagen</h2>
    <p class="range-sub">MIRATONE NG Full-Color-Touch</p>
    <div class="products">
      <div class="product" role="img" aria-label="Bedieneinheit, Variante 1"></div>
      <div class="product" role="img" aria-label="Bedieneinheit, Variante 2"></div>
      <div class="product" role="img" aria-label="Bedieneinheit, Variante 3"></div>
    </div>
    <div class="tap-photo" role="img" aria-label="Foto von Zapfhähnen an einer Bar"></div>
    <div class="references">
      <span class="reference"><span class="dot"></span>Lindenkrug</span>
      <span class="reference">Tannhof</span>
      <span class="reference">Gondelhof</span>
    </div>
  </section>
</div>
</body>
</html>
```